Classic Minimalistic Business Card

Design a classic, minimalistic Business Card. Please find inspiration in the attached Classic Minimalistic examples. My information:
Name: Glen Ovamir
Company: Ovamir Capital
Logo: OC
Address: 1470 N Thornwick Rd, Suite 210 | Larkfield, OH 44910
Phone: 555-555-0192
Email: glenovamir@pvt.insure
Slogan: Building Strength Through Capital

Feel free to leave out any of the information above except my name.

I have selected Double-sided, but I am also open to Single-sided

Target Market(s)

22-70. income greater than 150k/year

Industry/Entity Type

Finance

Contact Information for Business Card

See Project Description

Requirements
Must have
• Ivory or "antiqued" background similar to the reference pictures

```html
<!DOCTYPE html>
<html lang="en">
<head>
<meta charset="utf-8">
<title>Ovamir Capital – Business Card</title>
<link href="https://fonts.googleapis.com/css2?family=Poppins:wght@400;600&display=swap" rel="stylesheet">
<style>
  :root {
    --page-bg: #e6e4e1;
    --card-ivory: #f3ede8;
    --card-ivory-deep: #ebe2dc;
    --panel-grey: #47474d;
    --panel-edge: #2c2c2f;
    --ink: #4a4a50;
    --text-light: #ffffff;
  }
  * { margin: 0; padding: 0; box-sizing: border-box; }
  html, body {
    width: 1200px; height: 900px; overflow: hidden;
    background: var(--page-bg);
    font-family: "Poppins", sans-serif;
  }
  .card {
    position: absolute; left: 100px; top: 141px;
    width: 1000px; height: 618px;
    overflow: hidden;
    box-shadow: 0 18px 40px rgba(0,0,0,0.18);
  }
  .card-shapes { position: absolute; inset: 0; }
  .brand {
    position: absolute; left: 0; top: 0; width: 440px;
    display: flex; flex-direction: column; align-items: center;
  }
  .brand-mark {
    margin-top: 104px;
    width: 118px; height: 118px; border-radius: 50%;
    border: 4px solid var(--ink);
  }
  .brand-name {
    margin-top: 28px;
    font-size: 33px; font-weight: 400; letter-spacing: 3px;
    color: var(--ink); text-transform: uppercase; white-space: nowrap;
  }
  .contact {
    position: absolute; left: 531px; top: 0;
    color: var(--text-light);
  }
  .contact-name {
    position: absolute; top: 150px; white-space: nowrap;
    font-size: 39px; font-weight: 600; letter-spacing: 0.3px;
    text-transform: uppercase;
  }
  .contact-line {
    position: absolute; white-space: nowrap;
    display: flex; align-items: center; gap: 12px;
    font-size: 29px; font-weight: 400;
  }
  .contact-line svg { width: 26px; height: 26px; flex: none; }
  .phone { top: 264px; }
  .email { top: 300px; }
  .address {
    position: absolute; top: 396px; white-space: nowrap;
    font-size: 29px; font-weight: 400; line-height: 37px;
  }
</style>
</head>
<body>
  <div class="card">
    <svg class="card-shapes" width="1000" height="618" viewBox="0 0 1000 618">
      <defs>
        <linearGradient id="ivoryTone" x1="0" y1="0" x2="1" y2="1">
          <stop offset="0" stop-color="var(--card-ivory)"/>
          <stop offset="1" stop-color="var(--card-ivory-deep)"/>
        </linearGradient>
      </defs>
      <rect width="1000" height="618" fill="url(#ivoryTone)"/>
      <path d="M440,0 L1000,0 L1000,618 L458,618 C400,520 400,420 450,320 C495,230 515,110 440,0 Z" fill="var(--panel-edge)"/>
      <path d="M485,0 L1000,0 L1000,618 L458,618 C400,520 400,420 450,320 C492,238 522,118 485,0 Z" fill="var(--panel-grey)"/>
    </svg>

    <div class="brand">
      <div class="brand-mark"></div>
      <div class="brand-name">Ovamir Capital</div>
    </div>

    <div class="contact">
      <div class="contact-name">Glen Ovamir</div>
      <div class="contact-line phone">
        <svg viewBox="0 0 24 24" fill="none" stroke="#fff" stroke-width="2" stroke-linecap="round" stroke-linejoin="round">
          <path d="M6.5 3.5l3 3.5-2 2a12 12 0 0 0 7.5 7.5l2-2 3.5 3-2 2.5C11 20 4 13 4 5.5z"/>
          <path d="M14 3a7 7 0 0 1 7 7"/><path d="M14 7a3 3 0 0 1 3 3"/>
        </svg>
        <span>555-555-0192</span>
      </div>
      <div class="contact-line email">
        <svg viewBox="0 0 24 24" fill="#fff">
          <path d="M2 6h20v12H2z"/>
          <path d="M2 6l10 7 10-7" fill="none" stroke="var(--panel-grey)" stroke-width="1.6"/>
        </svg>
        <span>glenovamir@pvt.insure</span>
      </div>
      <div class="address">1470 N Thornwick Rd,<br>Suite 210 | Larkfield, OH 44910</div>
    </div>
  </div>
</body>
</html>
```